Data Analytics Platform Website Design

Website design for a new data analytics platform called Metrica Core. I need a design that is simple but informative, professional but still sexy and that is aimed at the business professional instead of being "technical". I have a logo (picture uploaded) and also screenshots from the platform itself and I can also provide example websites from competitors that are similar in design and layout to what I need. I also have the messaging but I need help with photos, icons, font, layout, etc. I want to utilize some of the colors in the logo, but I want the overall color scheme to utilize darker blues (more serious feeling, less playful) with one accent color for highlighting. This design cannot be "fun", "playful", or "cheerful" and should instead be "professional", "serious", but still uncluttered and clean cut. However, simple does not mean easy because I want to see transitions that are clean and high level. I want the final design to be all of that while showing the company and our product as capable, serious, and reliable.

Example websites:
1. www.valdrenix.com
2. q7.ai
3. corvelane.com
4. https://www.pym.com/en_us/software/lorsa.html
5. https://www.belvoro.com/
6. gwendel.ai

Target Market(s)

Business Professionals - Government/large companies/data analytics focused

Industry/Entity Type

Data Science

Number of Pages Required

3 page

Font styles to use
Serif
Sans Serif

Requirements
Must have
• It must be clean and professional. Cannot be cluttered or too "busy". No playful or childish looks at all.
Nice to have
• I want to see professional designs but also professional concepts incorporated.
Should not have
• Should not have Comic Sans or the like, no playful or "techy" themes

```html
<!DOCTYPE html>
<html lang="en">
<head>
<meta charset="utf-8">
<title>Metrica Core — Data Analytics</title>
<link rel="stylesheet" href="https://fonts.googleapis.com/css2?family=Montserrat:wght@400;500;600;700;800&family=Poppins:wght@300;400&family=Open+Sans:wght@400;600&display=swap">
<style>
:root{
  --bg:#1c1b2e;
  --bg-deep:#171628;
  --panel:#211f35;
  --line:#34324c;
  --accent:#2f7bf0;
  --accent-soft:#3d86f5;
  --text:#ffffff;
  --muted:#c9c8d6;
  --dim:#8f8ea3;
}
*{margin:0;padding:0;box-sizing:border-box}
html,body{width:1200px;height:3790px;overflow:hidden}
body{background:var(--bg);color:var(--text);font-family:"Open Sans",sans-serif;position:relative}
.abs{position:absolute}
h1,h2,h3,h4{font-family:"Montserrat",sans-serif}
.btn{position:absolute;background:var(--accent);color:#fff;font-family:"Montserrat",sans-serif;font-weight:500;display:flex;align-items:center;justify-content:center;text-decoration:none}

/* header */
.brand{display:flex;align-items:center;gap:12px;font-family:"Poppins",sans-serif;font-weight:300;letter-spacing:1.5px;color:#fff}
.brand-mark{width:30px;height:30px;background:var(--accent)}
.site-header .brand{left:131px;top:31px;font-size:34px}
.nav{left:443px;top:40px;display:flex;gap:0;font-family:"Montserrat",sans-serif;font-size:15px;font-weight:500}
.nav a{color:#fff;text-decoration:none;position:absolute;white-space:nowrap}
.nav a.active{color:var(--accent-soft);text-decoration:underline}
.trial{left:972px;top:35px;width:97px;height:33px;border:2px solid var(--accent);color:var(--accent-soft);font-family:"Montserrat",sans-serif;font-weight:600;font-size:15px;display:flex;align-items:center;justify-content:center}

/* hero */
.hero-bg{left:0;top:0;width:1200px;height:720px;background:
  radial-gradient(ellipse 520px 260px at 170px 430px,rgba(47,123,240,.30),transparent 70%),
  radial-gradient(ellipse 700px 200px at 600px 620px,rgba(60,140,190,.18),transparent 70%),
  linear-gradient(180deg,#1a1a2c 0%,#18233a 55%,#1c1b2e 100%)}
.hero-title{left:131px;top:256px;font-size:32px;font-weight:800;letter-spacing:.5px}
.hero-sub{left:131px;top:314px;width:300px;font-family:"Montserrat",sans-serif;font-size:18px;line-height:26px;font-weight:500}
.hero .btn{left:132px;top:396px;width:140px;height:42px;font-size:17px}

.app{left:494px;top:150px;width:706px;height:454px;overflow:hidden;box-shadow:0 20px 50px rgba(0,0,0,.5)}
.app-side{position:absolute;left:0;top:0;width:138px;height:454px;background:#1e2030;font-size:7px;color:#9a9cb0}
.app-side .ttl{position:absolute;left:12px;top:10px;font-size:10px;color:#e3e4ee}
.app-side .item{position:absolute;left:12px;display:flex;align-items:center;gap:7px}
.app-side .item i{width:8px;height:8px;background:#4a5a8a;display:block}
.app-side .grp{position:absolute;left:12px;font-size:5px;color:#5a5c70;letter-spacing:.5px}
.app-main{position:absolute;left:138px;top:0;width:568px;height:454px;background:#eef0f5}
.app-top{position:absolute;left:0;top:0;width:568px;height:30px;background:#fff;border-bottom:1px solid #e2e4ea;font-size:7px;color:#555}
.app-card{position:absolute;left:10px;top:42px;width:558px;height:310px;background:#fff}
.app-foot{position:absolute;left:0;top:430px;width:568px;height:24px;background:#fff;font-size:6px;color:#777}

/* features */
.sec-title{left:0;width:1200px;text-align:center;font-size:23px;font-weight:700;letter-spacing:.3px}
.sec-rule{width:40px;height:2px;background:var(--accent);left:580px}
.feature{top:848px;height:342px;border:1px solid var(--line);text-align:center}
.feature svg{position:absolute;left:50%;top:30px;transform:translateX(-50%)}
.feature h3{position:absolute;left:0;right:0;top:134px;font-size:16px;font-weight:600;line-height:22px}
.feature p{position:absolute;left:22px;right:22px;top:196px;font-size:13px;line-height:19.5px;color:var(--muted)}

/* welcome */
.photo{background-size:cover}
.welcome-photo{left:0;top:1278px;width:678px;height:406px;background:linear-gradient(135deg,#5b6b80 0%,#c9d1dc 40%,#eef1f5 60%,#9aa6b4 100%)}
.eyebrow{left:723px;top:1309px;font-size:18px;font-weight:700}
.welcome-title{left:722px;top:1334px;font-size:31px;font-weight:800}
.body-copy{font-size:15px;line-height:22.4px;color:var(--muted)}
.welcome-copy{left:725px;top:1401px;width:345px}
.welcome .btn{left:728px;top:1612px;width:140px;height:44px;font-size:17px}

.pillar{top:1751px;height:174px;background:#211f33}
.pillar h4{position:absolute;left:32px;top:38px;font-size:15px;font-weight:600}
.pillar p{position:absolute;left:32px;top:72px;width:250px;font-size:13px;line-height:19.5px;color:var(--dim)}

/* performance */
.perf-bg{left:0;top:2003px;width:1200px;height:484px;background:linear-gradient(90deg,#3a3b6a 0%,#2e3058 45%,#1b2140 70%,#142036 100%)}
.perf-photo{left:573px;top:2003px;width:627px;height:484px;background:radial-gradient(ellipse 300px 200px at 300px 230px,rgba(47,123,240,.35),transparent 70%),linear-gradient(180deg,#1d2a44 0%,#14223a 100%)}
.perf-title{left:131px;top:2064px;font-size:23px;font-weight:800;line-height:35px}
.perf-copy{left:131px;top:2157px;width:345px}
.perf .btn{left:131px;top:2366px;width:139px;height:43px;font-size:17px}

/* resources */
.res{top:2647px;width:293px}
.res .photo{width:293px;height:172px}
.res h4{margin-top:30px;font-size:15px;font-weight:600;line-height:19.5px}
.res p{margin-top:11px;font-size:11.5px;line-height:16px;color:var(--muted)}
.res .btn{position:static;margin-top:20px;width:88px;height:27px;font-size:12px}

/* cta */
.cta-bg{left:0;top:3063px;width:1200px;height:374px;background:linear-gradient(180deg,#1e1d31 0%,#222437 50%,#1a1a2c 100%)}
.cta-title{left:0;top:3160px;width:1200px;text-align:center;font-size:20px;font-weight:800}
.cta-copy{left:0;top:3210px;width:1200px;text-align:center;font-size:17px;line-height:24px;color:var(--muted)}
.cta .btn{left:531px;top:3293px;width:138px;height:44px;font-size:17px}

/* footer */
.footer-bg{left:0;top:3437px;width:1200px;height:353px;background:var(--bg-deep)}
.site-footer .brand{left:131px;top:3535px;font-size:32px}
.f-head{top:3490px;font-family:"Montserrat",sans-serif;font-size:12px;font-weight:700;letter-spacing:.5px}
.f-menu{left:479px;top:3530px;font-size:12px;line-height:20px;list-style:none}
.contact-row{display:flex;gap:10px;align-items:flex-start;font-size:12px;line-height:16px;position:absolute}
.icon-dot{width:22px;height:22px;border-radius:50%;background:#fff;flex:none;display:flex;align-items:center;justify-content:center}
.f-rule{left:131px;top:3721px;width:938px;height:1px;background:var(--line)}
.copyright{left:0;top:3748px;width:1200px;text-align:center;font-size:10px;color:var(--muted)}
</style>
</head>
<body>

<!-- Header -->
<header class="site-header">
  <div class="brand abs"><span class="brand-mark"></span>Metrica Core</div>
  <nav class="nav abs">
    <a class="active" style="left:0">Home</a>
    <a style="left:81px">About us</a>
    <a style="left:184px">Solutions</a>
    <a style="left:296px">Resources</a>
    <a style="left:409px">Contact Us</a>
  </nav>
  <div class="trial abs">Free Trial</div>
</header>

<!-- Hero -->
<section class="hero">
  <div class="hero-bg abs" role="img" aria-label="Dark backdrop of glowing blue data particles flowing in waves"></div>
  <h1 class="hero-title abs">DATA ANALYTICS</h1>
  <p class="hero-sub abs">Lorem Ipsum is simply dummy text of the printing.</p>
  <a class="btn">Read More</a>

  <div class="app abs">
    <div class="app-side">
      <div class="ttl">Metrica Core</div>
      <div class="item" style="top:48px;color:#cdd3ef"><i style="background:#3d6ee0"></i>Organization</div>
      <div class="item" style="top:72px"><i></i>Security Keys</div>
      <div class="grp" style="top:104px">TOOLS &amp; GUIDES</div>
      <div class="item" style="top:125px"><i></i>Learning Center</div>
      <div class="item" style="top:149px"><i></i>Workbench</div>
      <div class="item" style="top:173px"><i></i>Jobs</div>
      <div class="item" style="top:197px"><i></i>Wiki</div>
      <div class="grp" style="top:229px">DATA MANAGEMENT</div>
      <div class="item" style="top:250px"><i></i>Data Lakes</div>
      <div class="item" style="top:274px"><i></i>Files</div>
      <div class="item" style="top:298px"><i></i>Databases</div>
      <div class="item" style="top:322px"><i></i>Streams</div>
      <div class="item" style="top:346px"><i></i>Admin</div>
      <div class="grp" style="top:378px">DATA INTELLIGENCE</div>
      <div class="item" style="top:399px"><i></i>Overview</div>
      <div class="item" style="top:423px"><i></i>Spotlight</div>
    </div>
    <div class="app-main">
      <div class="app-top">
        <span class="abs" style="left:20px;top:11px">Dashboard</span>
        <span class="abs" style="left:78px;top:11px">Builder</span>
        <span class="abs" style="left:120px;top:11px">Library</span>
        <span class="abs" style="left:166px;top:11px">Widgets</span>
        <span class="abs" style="left:216px;top:11px">Custom</span>
        <svg class="abs" style="left:380px;top:9px" width="180" height="12"><circle cx="6" cy="6" r="4" fill="none" stroke="#3d6ee0"/><rect x="30" y="2" width="8" height="8" fill="#3d6ee0"/><rect x="56" y="2" width="8" height="8" fill="#6a9cf0"/><rect x="82" y="2" width="8" height="8" fill="#3d6ee0"/><rect x="108" y="2" width="8" height="8" fill="#8fa3c8"/><rect x="134" y="2" width="8" height="8" fill="#c8506a"/></svg>
      </div>
      <div class="app-card">
        <div class="abs" style="left:18px;top:16px;font-size:9px;color:#333;font-weight:600">Organization Administration</div>
        <div class="abs" style="left:0;top:40px;width:558px;height:1px;background:#e6e8ee"></div>
        <div class="abs" style="left:30px;top:58px;font-size:7px;color:#777">Organization</div>
        <div class="abs" style="left:108px;top:58px;font-size:7px;color:#777">Users</div>
        <div class="abs" style="left:178px;top:58px;font-size:7px;color:#3d6ee0">Environments</div>
        <div class="abs" style="left:170px;top:69px;width:70px;height:1px;background:#3d6ee0"></div>
        <div class="abs" style="left:30px;top:78px;width:520px;height:30px;background:#f3f5f9"></div>
        <div class="abs" style="left:65px;top:90px;font-size:6px;color:#555">The example form below shows common form elements with updated styles applied.</div>
        <div class="abs" style="left:44px;top:134px;width:54px;height:17px;background:#3d6ee0;color:#fff;font-size:6px;display:flex;align-items:center;justify-content:center">+ Create</div>
        <div class="abs" style="left:44px;top:168px;width:106px;height:18px;border:1px solid #dde0e8"></div>
        <div class="abs" style="left:44px;top:200px;width:500px;height:1px;background:#eceef3"></div>
        <div class="abs" style="left:44px;top:218px;width:500px;height:1px;background:#eceef3"></div>
        <div class="abs" style="left:86px;top:226px;font-size:6px;color:#333">test</div>
        <div class="abs" style="left:258px;top:226px;font-size:6px;color:#333">env-kcu4e</div>
        <div class="abs" style="left:44px;top:244px;width:500px;height:1px;background:#eceef3"></div>
        <svg class="abs" style="left:44px;top:258px" width="100" height="14"><rect x="0" y="1" width="12" height="12" fill="none" stroke="#dde0e8"/><rect x="17" y="1" width="12" height="12" fill="none" stroke="#dde0e8"/><rect x="34" y="1" width="12" height="12" fill="#3d6ee0"/><rect x="51" y="1" width="12" height="12" fill="none" stroke="#dde0e8"/><rect x="68" y="1" width="12" height="12" fill="none" stroke="#dde0e8"/></svg>
      </div>
      <div class="app-foot"><span class="abs" style="left:14px;top:8px">About &nbsp; Team &nbsp; Contact</span></div>
    </div>
  </div>
</section>

<!-- Features -->
<section class="features">
  <h2 class="sec-title abs" style="top:752px">FEATURES</h2>
  <div class="sec-rule abs" style="top:797px"></div>

  <article class="feature abs" style="left:129px;width:221px">
    <svg width="66" height="76" viewBox="0 0 66 76"><path d="M33 4C16 4 6 16 6 30c0 8 3 13 7 18v24h28v-10h10c4 0 6-3 6-6v-8l6-2-6-12C57 17 48 4 33 4z" fill="var(--accent)"/><g stroke="#1c1b2e" stroke-width="2" fill="none"><circle cx="24" cy="24" r="3"/><circle cx="40" cy="20" r="3"/><circle cx="34" cy="36" r="3"/><circle cx="20" cy="40" r="3"/><path d="M27 24l10-3M38 23l-3 10M31 37l-8 2M24 27l-3 10"/></g></svg>
    <h3>Intelligent<br>Observability</h3>
    <p>There are many variations of passages of Lorem Ipsum available, but the majority have suffered alteration in some form, by inject humour.</p>
  </article>

  <article class="feature abs" style="left:372px;width:221px">
    <svg width="72" height="72" viewBox="0 0 72 72"><g fill="none" stroke="var(--accent)" stroke-width="3"><path d="M31 4h10l2 9 7 3 8-5 7 7-5 8 3 7 9 2v10l-9 2-3 7 5 8-7 7-8-5-7 3-2 9H31l-2-9-7-3-8 5-7-7 5-8-3-7-9-2V31l9-2 3-7-5-8 7-7 8 5 7-3z"/><circle cx="36" cy="36" r="17"/><path d="M28 36l6 6 11-12"/></g></svg>
    <h3>Continuous<br>automation</h3>
    <p>There are many variations of passages of Lorem Ipsum available, but the majority have suffered alteration in some form, by inject humour.</p>
  </article>

  <article class="feature abs" style="left:612px;width:220px">
    <svg width="80" height="72" viewBox="0 0 80 72"><g fill="none" stroke="var(--accent)" stroke-width="3"><text x="24" y="28" font-family="Montserrat,sans-serif" font-size="24" font-weight="700" fill="var(--accent)" stroke="none">AI</text><path d="M8 8h10M6 16h8M60 8h12M62 18h10M6 40l18 8h22c4 0 4 6 0 6H30M6 56l20 10h30l20-16c2-4-2-7-6-5L56 54"/></g></svg>
    <h3>AI-assistance</h3>
    <p>There are many variations of passages of Lorem Ipsum available, but the majority have suffered alteration in some form, by inject humour.</p>
  </article>

  <article class="feature abs" style="left:846px;width:220px">
    <svg width="80" height="72" viewBox="0 0 80 72"><rect x="4" y="6" width="72" height="46" fill="var(--accent)"/><rect x="10" y="12" width="60" height="34" fill="#1c1b2e"/><rect x="16" y="32" width="5" height="10" fill="var(--accent)"/><rect x="24" y="26" width="5" height="16" fill="var(--accent)"/><rect x="32" y="20" width="5" height="22" fill="var(--accent)"/><circle cx="54" cy="29" r="10" fill="var(--accent)"/><path d="M54 29V19a10 10 0 0 1 10 10z" fill="#1c1b2e"/><rect x="34" y="52" width="12" height="10" fill="var(--accent)"/><rect x="24" y="62" width="32" height="5" fill="var(--accent)"/></svg>
    <h3>User experience &amp;<br>business analytics</h3>
    <p>There are many variations of passages of Lorem Ipsum available, but the majority have suffered alteration in some form, by inject humour.</p>
  </article>
</section>

<!-- Welcome -->
<section class="welcome">
  <div class="welcome-photo photo abs" role="img" aria-label="Hands holding a tablet showing financial report charts"></div>
  <div class="eyebrow abs">WELCOME TO</div>
  <h2 class="welcome-title abs">METRICA CORE</h2>
  <p class="welcome-copy body-copy abs">Lorem ipsum dolor sit amet, consectetur adipis cing elit, sed do eiusmod tempor incididunt ut labore et dolore magna aliqua. Ut enim ad minim veniam, quis nostrud exercitation ullamco laboris nisi ut aliquip ex ea commodo consequat. Duis aute irure dolor in reprehenderit in volup tate velit esse cillum dolore eu fugiat nulla pariatur. Excepteur sint .</p>
  <a class="btn">Read More</a>

  <article class="pillar abs" style="left:126px;width:312px"><h4>Real-Time Visibility</h4><p>There are many variations of passages of Lorem Ipsum available, but the majority have suffered alteration in some form, by inject humour.</p></article>
  <article class="pillar abs" style="left:448px;width:306px"><h4>Comprehensive Control</h4><p>There are many variations of passages of Lorem Ipsum available, but the majority have suffered alteration in some form, by inject humour.</p></article>
  <article class="pillar abs" style="left:768px;width:307px"><h4>Rapid Response</h4><p>There are many variations of passages of Lorem Ipsum available, but the majority have suffered alteration in some form, by inject humour.</p></article>
</section>

<!-- Performance -->
<section class="perf">
  <div class="perf-bg abs"></div>
  <div class="perf-photo abs" role="img" aria-label="Businessman holding a glowing tablet projecting a rising stock chart"></div>
  <h2 class="perf-title abs">MAXIMIZE PERFORMANCE,<br>MINIMIZE RISK</h2>
  <p class="perf-copy body-copy abs" style="color:#e0e0ea">Lorem ipsum dolor sit amet, consectetur adipis cing elit, sed do eiusmod tempor incididunt ut labore et dolore magna aliqua. Ut enim ad minim veniam, quis nostrud exercitation ullamco laboris nisi ut aliquip ex ea commodo consequat. Duis aute irure dolor in reprehenderit in volup tate velit esse cillum dolore eu fugiat nulla pariatur. Excepteur sint .</p>
  <a class="btn">Read More</a>
</section>

<!-- Resources -->
<section class="resources">
  <h2 class="sec-title abs" style="top:2553px">RESOURCES</h2>
  <div class="sec-rule abs" style="top:2599px"></div>

  <article class="res abs" style="left:131px">
    <div class="photo" role="img" aria-label="Analyst at a desk reviewing dashboards on a monitor" style="background:linear-gradient(135deg,#b9c7d6 0%,#4d6a8c 45%,#1f3550 100%)"></div>
    <h4>Lorem ipsum dolor sit amet conse ctetur adipiscing</h4>
    <p>Lorem ipsum dolor sit amet, consectetur adipis cing elit, sed do eiusmod tempor incididunt ut labore et dolore magna aliqua.</p>
    <a class="btn">Read More</a>
  </article>
  <article class="res abs" style="left:453px">
    <div class="photo" role="img" aria-label="Hands holding a glowing cloud network graphic" style="background:radial-gradient(circle at 50% 40%,#c9a57a 0%,#30476a 30%,#14243c 75%)"></div>
    <h4>Lorem ipsum dolor sit amet conse ctetur adipiscing</h4>
    <p>Lorem ipsum dolor sit amet, consectetur adipis cing elit, sed do eiusmod tempor incididunt ut labore et dolore magna aliqua.</p>
    <a class="btn">Read More</a>
  </article>
  <article class="res abs" style="left:776px">
    <div class="photo" role="img" aria-label="Person typing on a laptop with data overlay" style="background:linear-gradient(135deg,#9aa6b4 0%,#3a4556 50%,#1a2030 100%)"></div>
    <h4>Lorem ipsum dolor sit amet conse ctetur adipiscing</h4>
    <p>Lorem ipsum dolor sit amet, consectetur adipis cing elit, sed do eiusmod tempor incididunt ut labore et dolore magna aliqua.</p>
    <a class="btn">Read More</a>
  </article>
</section>

<!-- Call to action -->
<section class="cta">
  <div class="cta-bg abs" role="img" aria-label="Faint dark image of hands on a laptop keyboard"></div>
  <h2 class="cta-title abs">LOREM IPSUM DOLOR SIT AMET CONSECTETUR ADIPISCING ELIT</h2>
  <p class="cta-copy abs">But I must explain to you how all this mistaken idea of denouncing pleasure and praising<br>pain was born and I will give you a complete account of the system</p>
  <a class="btn">Contact Us</a>
</section>

<!-- Footer -->
<footer class="site-footer">
  <div class="footer-bg abs"></div>
  <div class="brand abs"><span class="brand-mark"></span>Metrica Core</div>

  <div class="f-head abs" style="left:479px">MENU</div>
  <ul class="f-menu abs"><li>HOME</li><li>ABOUT US</li><li>SOLUTIONS</li><li>RESOURCES</li><li>CONTACT US</li></ul>

  <div class="f-head abs" style="left:696px">CONTACT US</div>
  <div class="contact-row" style="left:694px;top:3530px">
    <span class="icon-dot"><svg width="10" height="12" viewBox="0 0 10 12"><path d="M5 0a4.5 4.5 0 0 0-4.5 4.5C.5 8 5 12 5 12s4.5-4 4.5-7.5A4.5 4.5 0 0 0 5 0z" fill="#1c1b2e"/><circle cx="5" cy="4.5" r="1.6" fill="#fff"/></svg></span>
    <span>2750 Larkmoor Avenue<br>Delvin, CA 90218</span>
  </div>
  <div class="contact-row" style="left:694px;top:3581px">
    <span class="icon-dot"><svg width="11" height="11" viewBox="0 0 12 12"><path d="M2.5 0.5l2 2.5-1 1.5a7 7 0 0 0 4 4l1.5-1 2.5 2-1 2C5 11.5.5 7 .5 1.5z" fill="#1c1b2e"/></svg></span>
    <span>Call Us<br>555.0142.317</span>
  </div>
  <div class="contact-row" style="left:694px;top:3632px">
    <span class="icon-dot"><svg width="11" height="9" viewBox="0 0 11 9"><rect x="0" y="0" width="11" height="9" fill="#1c1b2e"/><path d="M0.5 0.5l5 4 5-4" stroke="#fff" fill="none"/></svg></span>
    <span>E mail Us<br>info@MetricaCore.com</span>
  </div>

  <div class="f-head abs" style="left:959px">FOLLOW US</div>
  <div class="contact-row" style="left:957px;top:3530px"><span class="icon-dot"></span><span>Like us on<br>FRIENDLOOP</span></div>
  <div class="contact-row" style="left:957px;top:3581px"><span class="icon-dot"></span><span>Follow us on<br>CHIRPLINE</span></div>
  <div class="contact-row" style="left:957px;top:3632px"><span class="icon-dot"></span><span>Follow us on<br>WORKVINE</span></div>

  <div class="f-rule abs"></div>
  <div class="copyright abs">Copyright © 2021 All Rights Reserved</div>
</footer>

</body>
</html>
```